Colin Vesk Personal Card

I am looking for a personal card that has my contact information on the front and then the url for my website on the back. I am a fan of minimal, modern design, but am very open minded to other styles. Both portrait and landscape designs are acceptable. The only other specification that I have is that some sort of graphic of a raven is present somewhere on the card (my last name 'Vesk' means raven in German).
Industry/Entity Type
Landscape
Contact Information for Business Card
Colin Vesk
508.641.2093
colintvesk@postvale.com
colintvesk.com
Colors
Designer to choose colors to be used in the design.
Requirements
Must have
- Ornvale on some part of the card

```html
<!DOCTYPE html>
<html lang="en">
<head>
<meta charset="utf-8">
<title>Colin Vesk Personal Card</title>
<link rel="stylesheet" href="https://fonts.googleapis.com/css2?family=Lato:wght@400&display=swap">
<style>
  :root {
    --stage: #e4e4e4;
    --ink: #262829;
    --amber: #e09a26;
    --paper: #ffffff;
    --rule: #8a8a8a;
  }
  * { margin: 0; padding: 0; box-sizing: border-box; }
  html, body { width: 1200px; height: 920px; overflow: hidden; }
  body {
    background: var(--stage);
    font-family: "Lato", Arial, sans-serif;
    position: relative;
  }
  .card {
    position: absolute;
    box-shadow: 0 2px 6px rgba(0,0,0,0.25);
  }
  .card-back {
    left: 108px; top: 87px; width: 605px; height: 351px;
    background: var(--ink);
  }
  .card-front {
    left: 499px; top: 484px; width: 614px; height: 356px;
    background: var(--paper);
    overflow: hidden;
  }
  .brand-dot {
    position: absolute;
    border-radius: 50%;
    background: var(--amber);
  }
  .brand-name {
    position: absolute;
    font-weight: 400;
    line-height: 1;
    letter-spacing: 1px;
    white-space: nowrap;
  }
  .card-back .brand-dot { left: 262px; top: 108px; width: 84px; height: 84px; }
  .card-back .brand-name {
    left: 0; width: 605px; text-align: center; top: 182px;
    font-size: 56px; color: var(--paper);
  }
  .back-url {
    position: absolute; left: 0; width: 605px; top: 307px;
    text-align: center; font-size: 15px; color: var(--paper);
  }
  .card-front .brand-dot { left: 160px; top: 104px; width: 84px; height: 84px; }
  .card-front .brand-name {
    left: 92px; width: 220px; text-align: center; top: 184px;
    font-size: 58px; color: var(--ink);
  }
  .divider {
    position: absolute; left: 327px; top: 114px; width: 1px; height: 142px;
    background: linear-gradient(var(--rule), rgba(138,138,138,0.2));
  }
  .holder { position: absolute; left: 350px; top: 124px; }
  .holder-name { font-size: 23px; color: var(--amber); line-height: 1.1; }
  .holder-role { font-size: 13px; color: var(--ink); margin-top: 1px; }
  .contact-list { position: absolute; left: 351px; top: 184px; list-style: none; }
  .contact-list li {
    display: flex; align-items: center; height: 18px;
    font-size: 14px; color: var(--ink);
  }
  .contact-list svg { width: 11px; height: 11px; margin-right: 10px; fill: var(--amber); }
  .swoosh { position: absolute; left: 0; bottom: 0; width: 614px; height: 40px; }
</style>
</head>
<body>
  <section class="card card-back">
    <span class="brand-dot"></span>
    <span class="brand-name">Ornvale</span>
    <p class="back-url">www.colintvesk.com</p>
  </section>

  <section class="card card-front">
    <span class="brand-dot"></span>
    <span class="brand-name">Ornvale</span>
    <span class="divider"></span>
    <div class="holder">
      <p class="holder-name">Colin Vesk</p>
      <p class="holder-role">Occupation</p>
    </div>
    <ul class="contact-list">
      <li><svg viewBox="0 0 12 12"><path d="M3 0h6a1 1 0 0 1 1 1v10a1 1 0 0 1-1 1H3a1 1 0 0 1-1-1V1a1 1 0 0 1 1-1zm0.5 1.5v8h5v-8z"/></svg>508.641.2093</li>
      <li><svg viewBox="0 0 12 12"><path d="M0 2h12v1L6 7 0 3z M0 4.5l6 4 6-4V10H0z"/></svg>colintvesk@postvale.com</li>
      <li><svg viewBox="0 0 12 12"><circle cx="6" cy="6" r="6"/></svg>www.colintvesk.com</li>
    </ul>
    <svg class="swoosh" viewBox="0 0 614 40" preserveAspectRatio="none">
      <path d="M0 18 Q 300 24 614 12 L614 40 L0 40 Z" fill="var(--ink)"/>
      <path d="M0 17 Q 300 23 614 10 L614 13 Q 300 25 0 19 Z" fill="var(--paper)"/>
      <path d="M120 16 Q 340 18 614 1 L614 9 Q 330 22 120 16 Z" fill="var(--amber)"/>
    </svg>
  </section>
</body>
</html>
```